Cobalt Ridge Mini Storage - Ad for half Page

Need half page ad for a publication.
would also like to be able to use in the future
self storage facility - 3 locations, the third opening soon
do not like real busy projects...i have a logo but willing to tweak if needed

```html
<!DOCTYPE html>
<html lang="en">
<head>
<meta charset="utf-8">
<title>Cobalt Ridge Mini Storage – Half Page Ad</title>
<link href="https://fonts.googleapis.com/css2?family=Alfa+Slab+One&family=Lato:wght@400;700;900&display=swap" rel="stylesheet">
<style>
  :root {
    --brown-dark: #5a2912;
    --brown-mid: #7a4219;
    --brown-light: #8e5424;
    --tan: #c38a4e;
    --sky: #f3f4f5;
    --white: #ffffff;
    --photo-green: #7fbf4d;
    --photo-grey: #c9cbc9;
    --text-light: #ffffff;
  }
  * { margin: 0; padding: 0; box-sizing: border-box; }
  html, body { width: 1200px; height: 912px; overflow: hidden; background: var(--white); }
  .ad {
    position: relative;
    width: 1200px;
    height: 912px;
    overflow: hidden;
    background: var(--sky);
    font-family: "Lato", Arial, sans-serif;
  }
  .ad-art { position: absolute; inset: 0; width: 1200px; height: 912px; }

  .brand {
    position: absolute;
    left: 556px;
    top: 66px;
    display: flex;
    align-items: center;
    gap: 30px;
  }
  .brand-square {
    width: 124px;
    height: 124px;
    background: var(--tan);
  }
  .brand-name {
    font-family: "Lato", Arial, sans-serif;
    font-weight: 900;
    font-size: 56px;
    line-height: 1.05;
    color: var(--brown-dark);
  }

  .locations {
    position: absolute;
    left: 497px;
    top: 400px;
    width: 420px;
    list-style: none;
  }
  .location {
    position: relative;
    height: 111px;
    padding-left: 54px;
    color: var(--text-light);
  }
  .location + .location::before {
    content: "";
    position: absolute;
    left: 54px;
    top: -8px;
    width: 361px;
    height: 1px;
    background: linear-gradient(90deg, rgba(255,255,255,0.55), rgba(255,255,255,0.1));
  }
  .location-pin {
    position: absolute;
    left: 0;
    top: 10px;
    width: 38px;
    height: 58px;
  }
  .location-address {
    font-size: 19px;
    line-height: 26px;
    font-weight: 400;
  }
  .location-phone {
    margin-top: 8px;
    font-size: 22px;
    font-weight: 700;
  }

  .headline-band {
    position: absolute;
    left: 0;
    top: 741px;
    width: 1200px;
    height: 171px;
    background: var(--white);
    display: flex;
    align-items: center;
    justify-content: center;
  }
  .headline {
    font-family: "Alfa Slab One", Georgia, serif;
    font-weight: 400;
    font-size: 88px;
    line-height: 1;
    color: var(--brown-dark);
    white-space: nowrap;
    margin-top: -6px;
  }
</style>
</head>
<body>
<main class="ad">
  <svg class="ad-art" viewBox="137 137 1226 865" preserveAspectRatio="none" aria-hidden="false">
    <defs>
      <linearGradient id="brownField" x1="0" y1="0" x2="1" y2="0">
        <stop offset="0" stop-color="#5a2912"/>
        <stop offset="0.45" stop-color="#5e2c13"/>
        <stop offset="1" stop-color="#8e5424"/>
      </linearGradient>
      <linearGradient id="warehouseTone" x1="0" y1="0" x2="1" y2="1">
        <stop offset="0" stop-color="#e6e4e0"/>
        <stop offset="0.6" stop-color="#d8cfc3"/>
        <stop offset="1" stop-color="#cfc9c2"/>
      </linearGradient>
      <linearGradient id="lockerTone" x1="0" y1="0" x2="1" y2="1">
        <stop offset="0" stop-color="#d9dcd6"/>
        <stop offset="0.5" stop-color="#8cc45a"/>
        <stop offset="1" stop-color="#5f9a3a"/>
      </linearGradient>
      <linearGradient id="aisleTone" x1="0" y1="0" x2="1" y2="1">
        <stop offset="0" stop-color="#cdd3c8"/>
        <stop offset="0.55" stop-color="#a9b98f"/>
        <stop offset="1" stop-color="#8a6a4a"/>
      </linearGradient>
    </defs>

    <polygon class="warehouse-photo" role="img" aria-label="Faded photo of a warehouse with shelves stacked with cardboard boxes"
      points="1363,240 1363,790 1060,470" fill="url(#warehouseTone)" opacity="0.85"/>

    <polygon class="brown-field"
      points="137,362 540,220 825,490 947,370 1363,790 1363,840 137,840" fill="url(#brownField)"/>

    <polygon class="accent-corner" points="137,660 320,840 137,840" fill="var(--tan)"/>
    <polygon class="accent-stripe" points="137,588 137,632 330,840 362,840" fill="var(--white)"/>

    <polygon class="photo-lockers" role="img" aria-label="Photo of a woman opening a green self storage locker"
      points="137,137 590,137 430,300 300,476 230,476 137,362" fill="url(#lockerTone)"/>

    <polygon class="frame-large" points="140,625 400,425 597,605 400,795" fill="var(--tan)"/>
    <polygon class="photo-moving" role="img" aria-label="Photo of a man moving stacked boxes on a hand truck into a storage unit"
      points="158,625 400,440 580,605 400,780" fill="url(#aisleTone)"/>

    <polygon class="frame-small" points="545,265 668,388 545,518 422,392" fill="var(--tan)"/>
    <polygon class="photo-consult" role="img" aria-label="Photo of a couple reviewing a tablet in a storage aisle"
      points="545,282 652,388 545,502 438,392" fill="url(#lockerTone)"/>
  </svg>

  <div class="brand">
    <div class="brand-square"></div>
    <div class="brand-name">Cobalt Ridge<br>Mini Storage</div>
  </div>

  <ul class="locations">
    <li class="location">
      <svg class="location-pin" viewBox="0 0 38 58"><path d="M19 3C10 3 3 10 3 19c0 12 16 33 16 33s16-21 16-33C35 10 28 3 19 3z" fill="none" stroke="#fff" stroke-width="3"/><circle cx="19" cy="19" r="7" fill="none" stroke="#fff" stroke-width="3"/></svg>
      <p class="location-address">Lorem ipsum dolor sit amet, consectetuer<br>adipiscing elit, sed diam nonummy nibh</p>
      <p class="location-phone">Ph: 0123 456 789</p>
    </li>
    <li class="location">
      <svg class="location-pin" viewBox="0 0 38 58"><path d="M19 3C10 3 3 10 3 19c0 12 16 33 16 33s16-21 16-33C35 10 28 3 19 3z" fill="none" stroke="#fff" stroke-width="3"/><circle cx="19" cy="19" r="7" fill="none" stroke="#fff" stroke-width="3"/></svg>
      <p class="location-address">Lorem ipsum dolor sit amet, consectetuer<br>adipiscing elit, sed diam nonummy nibh</p>
      <p class="location-phone">Ph: 0123 456 789</p>
    </li>
    <li class="location">
      <svg class="location-pin" viewBox="0 0 38 58"><path d="M19 3C10 3 3 10 3 19c0 12 16 33 16 33s16-21 16-33C35 10 28 3 19 3z" fill="none" stroke="#fff" stroke-width="3"/><circle cx="19" cy="19" r="7" fill="none" stroke="#fff" stroke-width="3"/></svg>
      <p class="location-address">Lorem ipsum dolor sit amet, consectetuer<br>adipiscing elit, sed diam nonummy nibh</p>
      <p class="location-phone">Ph: 0123 456 789</p>
    </li>
  </ul>

  <div class="headline-band">
    <h1 class="headline">Self Storage Facility</h1>
  </div>
</main>
</body>
</html>
```